New company aimed at high net worth individuals needs a stationery design

We need a stationery design for a new company that is offering High Net Worth Individuals around the world a bespoke philanthropy service (enabling them to realise their personal aspirations in 'tailored benevolence'). Not looking for a logo because we think 'Tailored Benevolence...' speaks for itself. Looking for a clean look that smacks of (understated) quality and reliability to the billionaires who open our letters and folders.

Target Market(s)

High Net Worth Individuals, millionaires, CEOs of Companies, stock brokers, asset managers. Extremely wealthy individuals.

Industry/Entity Type

It Company

Contact Information for Business Card

Dr Gerald Finchley. Tailored Benevolence...
17 Corlett Crescent, Ambermere Vale, Wessexshire, CV31 9PT.
gerald.finchley@tailoredbenevolex.co.uk
www.tailoredbenevolex.co.uk
In UK: 07983 604527
Global: +44 7983 604527

Font styles to use
Serif
Decorative

Requirements
Must have
• clean look (I used to like the Global Treasury Business cards!). understated air of high quality. however I think that I like 'Tailored Benevolence...' rather than 'Tailored Benevolence Ltd.' because the former hints (I think at least) that you are on a journey leading to somewhere that can be great. whole aim of company is to get inside the clients hearts and enable them to achieve their personal dreams of helping people. Wife thinks a thumbprint or handprint somewhere might be good (I know what she means but I am not convinced)
Nice to have
• I would like the stationery to bear the words 'Tailored Benevolence...' the three dots signify that this is going to lead somewhere, something is going to happen. I am thinking about a strapline for the letterhead and folder: your experience - your heart - your legacy.
Should not have
• must not look like a business card from a charity or NGO.

```html
<!DOCTYPE html>
<html lang="en">
<head>
<meta charset="utf-8">
<title>Tailored Benevolence – Presentation Folder</title>
<link rel="stylesheet" href="https://fonts.googleapis.com/css2?family=Jost:wght@300;400;600&display=swap">
<style>
  :root {
    --backdrop: #d9d9d9;
    --backdrop-light: #f2f2f2;
    --folder-black: #242323;
    --folder-edge: #1a1a1a;
    --map-tone: #3a3a3a;
    --text-white: #ffffff;
    --text-soft: #bdbdbd;
    --text-muted: #8a8a8a;
  }
  html, body {
    margin: 0;
    width: 1200px;
    height: 971px;
    overflow: hidden;
  }
  body {
    background: radial-gradient(ellipse at 60% 30%, var(--backdrop-light) 0%, var(--backdrop) 75%);
    font-family: "Jost", "Century Gothic", sans-serif;
    position: relative;
  }
  .folder-spread {
    position: absolute;
    left: 200px;
    top: 202px;
    width: 800px;
    height: 566px;
    display: flex;
    box-shadow: 0 18px 40px rgba(0,0,0,0.25);
  }
  .folder-panel {
    position: relative;
    width: 400px;
    height: 566px;
    background: var(--folder-black);
  }
  .back-cover {
    border-right: 1px solid var(--folder-edge);
  }
  .contact-block {
    position: absolute;
    left: 28px;
    bottom: 36px;
    color: var(--text-soft);
    font-size: 7px;
    font-style: normal;
    font-weight: 400;
    line-height: 1.5;
    letter-spacing: 0.02em;
  }
  .contact-name {
    color: var(--text-white);
    font-weight: 600;
    letter-spacing: 0.08em;
    text-transform: uppercase;
    margin: 0 0 6px;
  }
  .contact-line { margin: 0; }
  .contact-label { color: var(--text-white); font-weight: 600; }
  .contact-address { margin: 6px 0 0; color: var(--text-muted); }

  .brand-title {
    position: absolute;
    left: 130px;
    top: 156px;
    margin: 0;
    color: var(--text-white);
    font-weight: 400;
    font-size: 17px;
    letter-spacing: 0.05em;
    line-height: 1.1;
    white-space: nowrap;
  }
  .brand-strapline {
    position: absolute;
    left: 130px;
    top: 184px;
    margin: 0;
    color: var(--text-soft);
    font-size: 8px;
    font-weight: 400;
    letter-spacing: 0.03em;
  }
  .world-map-area {
    position: absolute;
    left: 50px;
    top: 250px;
    width: 330px;
    height: 190px;
  }
</style>
</head>
<body>
  <main class="folder-spread">
    <section class="folder-panel back-cover">
      <address class="contact-block">
        <p class="contact-name">Dr Gerald Finchley</p>
        <p class="contact-line"><span class="contact-label">T:</span> 07983 604527</p>
        <p class="contact-line"><span class="contact-label">E:</span> gf@tailoredbenevolex.co.uk</p>
        <p class="contact-line"><span class="contact-label">W:</span> www.tailoredbenevolex.co.uk</p>
        <p class="contact-address">17 Corlett Crescent, Ambermere Vale<br>Wessexshire, CV31 9PT, UK</p>
      </address>
    </section>
    <section class="folder-panel front-cover">
      <h1 class="brand-title">Tailored Benevolence…</h1>
      <p class="brand-strapline">Your Vision • Your Mark</p>
      <svg class="world-map-area" viewBox="0 0 330 190" role="img" aria-label="Faint world map silhouette">
        <defs>
          <radialGradient id="mapTone" cx="50%" cy="45%" r="60%">
            <stop offset="0%" stop-color="#3a3a3a" stop-opacity="0.9"/>
            <stop offset="100%" stop-color="#242323" stop-opacity="0"/>
          </radialGradient>
        </defs>
        <rect width="330" height="190" fill="url(#mapTone)"/>
      </svg>
    </section>
  </main>
</body>
</html>
```